Business Card Design

We are a commercial real estate brokerage in San Francisco, leasing office buildings downtown.
I would like a clean, elegant look. Simple but powerful .

Industry/Entity Type

Business

Contact Information for Business Card

Derek Hollings
lic# 02875140
415.287.6041
derek@vexa-commercial.com
vexa-commercial.com

```html
<!DOCTYPE html>
<html lang="en">
<head>
<meta charset="utf-8">
<title>Vexa Commercial — Business Card</title>
<link href="https://fonts.googleapis.com/css2?family=Source+Sans+3:wght@400;600;700&display=swap" rel="stylesheet">
<style>
  :root {
    --stage: #000000;
    --card: #ffffff;
    --brand-blue: #6a95c3;
    --ink: #3f4a4c;
    --mark-grey: #4f5b5c;
  }
  * { margin: 0; padding: 0; box-sizing: border-box; }
  html, body { width: 1200px; height: 900px; overflow: hidden; background: var(--stage); }
  body { position: relative; font-family: "Source Sans 3", sans-serif; }

  .card {
    position: absolute;
    top: 327px;
    width: 432px;
    height: 248px;
    background: var(--card);
    border-radius: 10px;
  }
  .card--front { left: 168px; }
  .card--back { left: 620px; }

  .wordmark {
    position: absolute;
    display: flex;
    align-items: center;
    color: var(--mark-grey);
    font-weight: 700;
  }
  .wordmark__square { background: var(--mark-grey); flex: none; }
  .wordmark__text { display: flex; flex-direction: column; line-height: 0.95; }
  .wordmark__name { letter-spacing: 0.02em; }
  .wordmark__descriptor { letter-spacing: 0.03em; }

  .card--front .wordmark { left: 22px; top: 100px; gap: 10px; }
  .card--front .wordmark__square { width: 34px; height: 34px; }
  .card--front .wordmark__name { font-size: 31px; }
  .card--front .wordmark__descriptor { font-size: 15px; }

  .card--back .wordmark { left: 58px; top: 75px; gap: 18px; }
  .card--back .wordmark__square { width: 76px; height: 76px; }
  .card--back .wordmark__name { font-size: 62px; }
  .card--back .wordmark__descriptor { font-size: 28px; }

  .contact { position: absolute; left: 215px; top: 66px; color: var(--ink); }
  .contact__name { color: var(--brand-blue); font-size: 16.5px; font-weight: 600; line-height: 20px; }
  .contact__licence { font-size: 13px; margin-top: 12px; line-height: 16px; }
  .contact__list { list-style: none; margin-top: 14px; }
  .contact__item { display: flex; align-items: center; gap: 5px; font-size: 13px; line-height: 16.5px; }
  .contact__icon { width: 9px; height: 9px; flex: none; fill: var(--brand-blue); }
</style>
</head>
<body>
  <section class="card card--front" aria-label="Business card front">
    <div class="wordmark">
      <span class="wordmark__square"></span>
      <span class="wordmark__text">
        <span class="wordmark__name">VEXA</span>
        <span class="wordmark__descriptor">COMMERCIAL</span>
      </span>
    </div>
    <div class="contact">
      <p class="contact__name">Derek Hollings</p>
      <p class="contact__licence">Lic# 02875140</p>
      <ul class="contact__list">
        <li class="contact__item">
          <svg class="contact__icon" viewBox="0 0 10 10" aria-hidden="true"><path d="M2.2 0.5 L3.8 2.6 L2.9 3.7 C3.6 5.1 4.8 6.3 6.3 7.1 L7.4 6.2 L9.5 7.8 L8.6 9.4 C4.6 9.2 0.8 5.4 0.6 1.4 Z"/></svg>
          415.287.6041
        </li>
        <li class="contact__item">
          <svg class="contact__icon" viewBox="0 0 10 10" aria-hidden="true"><path d="M0.5 2 H9.5 V8 H0.5 Z M1.2 2.6 L5 5.4 L8.8 2.6" stroke="#fff" stroke-width="0.8"/></svg>
          derek@vexa-commercial.com
        </li>
        <li class="contact__item">
          <svg class="contact__icon" viewBox="0 0 10 10" aria-hidden="true"><circle cx="5" cy="5" r="4.5"/><path d="M0.5 5 H9.5 M5 0.5 C3 3 3 7 5 9.5 M5 0.5 C7 3 7 7 5 9.5" stroke="#fff" stroke-width="0.7" fill="none"/></svg>
          vexa-commercial.com
        </li>
      </ul>
    </div>
  </section>

  <section class="card card--back" aria-label="Business card back">
    <div class="wordmark">
      <span class="wordmark__square"></span>
      <span class="wordmark__text">
        <span class="wordmark__name">VEXA</span>
        <span class="wordmark__descriptor">COMMERCIAL</span>
      </span>
    </div>
  </section>
</body>
</html>
```